Website incl. html for real estate project

We need the design and implementation of a website for a real estate project. Condominiums are built, which are sold.
We upload the sales brochure. The website should be based on the design of the sales brochure.
There are three houses with 5 apartments each. It should be rendered like this. The structure of the menu should be roughly as follows. Most information about the content is either in the appendix as a picture or in the brochure (PDF)):
Home (page 4-5 from the brochure)
House A
house B
house c
overview
basement
Municipal elections (page 6-7 in the brochure pdf)
Contact
Please use Roboto Regular as font.
And one page should give an overview of all apartments with the prices, the living space, etc. as on the file overview2.jpg.
If you go to the House A, House B, or House C menus, a page should come up with the details for that house only. The pages in the brochure are:
House A (Page 10-11)
House B (page 22-23)
House C (page 34-35)
The individual apartments should each be shown on a property page. There the plan / floor plan of the apartment and the pictures from the inside should be shown. As with the object page.jpg attachment.
Für die Designer... Mehr Zeit...
Coded - Design and coding required
1 page

```html
<!DOCTYPE html>
<html lang="de">
<head>
<meta charset="utf-8">
<title>Lindmark Immobilien AG – Wohnpark am Bach</title>
<link href="https://fonts.googleapis.com/css2?family=Roboto:wght@400;500;700&family=Open+Sans:wght@600&display=swap" rel="stylesheet">
<style>
  :root{
    --white:#ffffff;
    --ink:#555b61;
    --nav:#7a7f84;
    --brand:#1a6fa8;
    --footer:#0a8ed5;
    --footer-bottom:#3c9fd1;
    --rule:#2d4a5c;
  }
  *{box-sizing:border-box;margin:0;padding:0}
  html,body{width:1200px;height:954px;overflow:hidden;background:var(--white);font-family:"Roboto",sans-serif}
  .page{position:relative;width:1200px;height:954px}

  .site-header{position:absolute;left:0;top:0;width:1200px;height:86px;background:var(--white);box-shadow:0 1px 3px rgba(0,0,0,.05)}
  .brand{position:absolute;left:27px;top:30px;display:flex;align-items:center;gap:7px;color:var(--brand);font-weight:700;font-size:17px;letter-spacing:.5px}
  .brand-mark{width:10px;height:10px;background:var(--brand)}
  .main-nav a{position:absolute;top:34px;font-family:"Open Sans",sans-serif;font-weight:600;font-size:12.5px;letter-spacing:1.6px;color:var(--nav);text-decoration:none}
  .nav-home{left:175px}
  .nav-a{left:254px}
  .nav-b{left:353px}
  .nav-c{left:452px}
  .header-contact{position:absolute;left:783px;top:33px;display:flex;gap:18px;font-size:13px;color:var(--ink)}
  .header-icons{position:absolute;left:1106px;top:30px;display:flex;gap:20px}

  .gallery{position:absolute;left:0;top:86px;width:1200px;height:488px;display:flex}
  .gallery-panel{height:100%}
  .gallery-panel.one{width:390px;background:
      linear-gradient(90deg,rgba(80,80,90,.18) 0%,rgba(80,80,90,0) 12%),
      linear-gradient(180deg,#d6d6de 0%,#e2e2e8 35%,#d4d4da 62%,#a9a9ae 72%,#c4c4c9 100%)}
  .gallery-panel.two{width:405px;background:
      linear-gradient(90deg,rgba(255,255,255,0) 70%,rgba(190,175,160,.35) 100%),
      linear-gradient(180deg,#f0f0f1 0%,#e8e7e6 40%,#d8d5d2 62%,#9c948e 68%,#c9c6c3 100%)}
  .gallery-panel.three{width:405px;background:
      linear-gradient(90deg,rgba(255,255,255,0) 75%,rgba(160,150,140,.3) 100%),
      linear-gradient(180deg,#e9e9eb 0%,#e4e4e6 40%,#d6d6d7 58%,#3f3d3c 62%,#dedcda 66%,#bdbab7 100%)}

  .site-footer{position:absolute;left:0;top:574px;width:1200px;height:317px;background:var(--footer);color:var(--white)}
  .footer-col{position:absolute;top:86px}
  .footer-col h3{font-weight:700;font-size:22px;line-height:27px;margin-bottom:28px}
  .footer-col p{font-size:13.5px;line-height:27px}
  .footer-col ul{list-style:none}
  .footer-col li{font-size:13px;height:37px;line-height:15px}
  .footer-col.links li:nth-child(3){height:28px}
  .footer-col.contact li{height:27px;font-weight:500}
  .col-company{left:97px}
  .col-company h3{margin-bottom:20px}
  .col-project{left:351px}
  .col-links{left:606px}
  .col-contact{left:860px}

  .footer-bottom{position:absolute;left:0;top:891px;width:1200px;height:63px;background:var(--footer-bottom);color:var(--white)}
  .footer-bottom::before{content:"";position:absolute;left:97px;top:0;width:991px;height:1px;background:var(--rule)}
  .copyright{position:absolute;left:97px;top:26px;font-size:12px}
  .social{position:absolute;left:973px;top:25px;display:flex;gap:12px}
  .social span{width:12px;height:12px;border-radius:50%;background:var(--white)}
</style>
</head>
<body>
<div class="page">
  <header class="site-header">
    <div class="brand"><span class="brand-mark"></span>LINDMARK</div>
    <nav class="main-nav">
      <a class="nav-home" href="#">HOME</a><a class="nav-a" href="#">HOUSE A</a><a class="nav-b" href="#">HOUSE B</a><a class="nav-c" href="#">HOUSE C</a>
    </nav>
    <div class="header-contact"><span>+41 61 555 20 40</span><span>info@lindmark-immo.ch</span></div>
    <div class="header-icons">
      <svg width="20" height="20" viewBox="0 0 20 20" aria-label="Suche"><circle cx="8.5" cy="8.5" r="7" fill="none" stroke="#444" stroke-width="1.6"/><line x1="13.5" y1="13.5" x2="19" y2="19" stroke="#444" stroke-width="1.6"/></svg>
      <svg width="20" height="20" viewBox="0 0 20 20" aria-label="Menü"><g fill="none" stroke="#444" stroke-width="1.5"><rect x="1" y="1" width="7" height="7"/><rect x="12" y="1" width="7" height="7"/><rect x="1" y="12" width="7" height="7"/><rect x="12" y="12" width="7" height="7"/></g></svg>
    </div>
  </header>

  <section class="gallery">
    <div class="gallery-panel one" role="img" aria-label="Helle moderne Küche mit Kochinsel und Barhocker"></div>
    <div class="gallery-panel two" role="img" aria-label="Weisse Küche mit Kochinsel und Wandbild"></div>
    <div class="gallery-panel three" role="img" aria-label="Offene Küche mit langer Kochinsel und Holzhockern"></div>
  </section>

  <footer class="site-footer">
    <div class="footer-col col-company">
      <h3>Lindmark<br>Immobilien AG</h3>
      <p>Hochwertige und moderne<br>Eigentumswohnungen</p>
    </div>
    <div class="footer-col col-project">
      <h3>Wohnpark am Bach</h3>
      <ul><li>HOUSE A</li><li>HOUSE B</li><li>HOUSE C</li></ul>
    </div>
    <div class="footer-col col-links links">
      <h3>QuicK Links</h3>
      <ul><li>Overview</li><li>Basement</li><li>Municipal Elections</li><li>Contact</li></ul>
    </div>
    <div class="footer-col col-contact contact">
      <h3>Contact</h3>
      <ul><li>+41 61 555 20 40</li><li>info@lindmark-immo.ch</li></ul>
    </div>
  </footer>
  <div class="footer-bottom">
    <div class="copyright">Copyright © 2022 Lindmark Immobilien AG</div>
    <div class="social" aria-label="Soziale Netzwerke"><span></span><span></span><span></span><span></span><span></span></div>
  </div>
</div>
</body>
</html>
```